PSD website for property company

Please read the brief thoroughly.

We are looking for a new website for a property group that does property acquisitions, property development and property management.
They buy, build and lease core inner city industrial assets in Sydney, Australia.
They also invest in residential developments.

Site menu
- Home page
- Property – sub menus include – Leasing ; Projects ; Investments ; Property Management
- Capital and finance
- About
- Contact

They like this website
https://www.verlo.com.au/

They want the site to be clean, modern and bold.
They like few colors, even black and white is OK to submit

They have a logo and style guide and useable images here:
http://www.kumet.net/temp/PelorisWeb2019.zip
The zip file is also attached to this project.
We have supplied some images to give you an idea, but we will also require you to provide at least 3 extra images from stock photos.
Use your imagination.

I am expecting a lot of similar designs, so be aware the photos you choose will be really important.
They want really 3 good stock photos used and supplied without charge.
Please not too generic, I repeat the quality of the photos is important.
You may provide several photos (but not in multiple submissions please) and we will choose the best three to be provided.

The winner will be selected on a single home page design and required to provide;
All photos use in original format without charge
A second ‘standard page’ template design based on the winning home page design

```html
<!DOCTYPE html>
<html lang="en">
<head>
<meta charset="utf-8">
<title>Peloris – Property Development &amp; Construction</title>
<link rel="stylesheet" href="https://fonts.googleapis.com/css2?family=Archivo+Black&family=Arimo:wght@400;700&display=swap">
<style>
:root{
  --blue:#1a86d6;
  --blue-light:#3d9fe6;
  --ink:#222;
  --muted:#555;
  --dark:#3c3c3c;
  --darker:#333;
  --white:#fff;
}
*{box-sizing:border-box;margin:0;padding:0}
html,body{width:1200px;height:3632px;overflow:hidden}
body{position:relative;background:var(--white);font-family:'Arimo',sans-serif;color:var(--ink)}
.abs{position:absolute}
a{color:inherit;text-decoration:none}

/* hero */
.hero{left:0;top:0;width:1200px;height:539px;background:linear-gradient(180deg,#8fa8d6 0%,#7d8fbd 45%,#6f7a8e 75%,#5f7a55 100%)}
.hero-rule{left:0;width:1200px;height:1px;background:rgba(255,255,255,.7)}
.brand{left:0;width:1200px;top:18px;text-align:center;font-weight:700;font-size:44px;letter-spacing:10px;color:var(--white)}
.main-nav{left:0;width:1200px;top:92px;text-align:center;font-size:12.5px;font-weight:700;color:var(--white)}
.main-nav span{margin:0 16px}
.bracket{width:66px;height:328px;border:5px solid var(--white);top:166px}
.bracket.left{left:162px;border-right:none}
.bracket.right{left:954px;border-left:none}
.tagline{left:0;width:1200px;top:182px;text-align:center;font-size:27px;color:var(--white)}
.hero-title{left:0;width:1200px;top:252px;text-align:center;font-family:'Archivo Black',sans-serif;font-size:47px;line-height:54px;letter-spacing:5px;color:var(--white)}
.btn-invest{left:524px;top:424px;width:139px;height:44px;background:var(--blue);color:var(--white);font-size:15px;display:flex;align-items:center;justify-content:center}
.dot{top:436px;width:15px;height:15px;border-radius:50%;border:2px solid var(--white)}
.dot.on{background:radial-gradient(circle,var(--white) 35%,transparent 40%)}
.scroll-hint{left:589px;top:529px;width:23px;height:43px;border:2px solid var(--blue);border-radius:12px;background:var(--white)}
.scroll-hint i{position:absolute;left:8.5px;top:10px;width:2px;height:12px;background:var(--blue)}

/* stats */
.stats{left:0;top:681px;width:1200px;height:155px;background:linear-gradient(90deg,#2e73c2,#4b93d8 50%,#2e73c2)}
.stat{top:716px;height:85px;border:4px solid var(--white);color:var(--white);font-family:'Archivo Black',sans-serif;font-size:18px;line-height:22px;display:flex;align-items:center;padding-left:18px;gap:8px}

/* service cards */
.card-photo{width:254px;height:170px}
.card-label{background:var(--white);color:var(--ink);font-size:18px;line-height:21px;padding:4px 14px}
.card-label.blue{color:var(--blue)}
.card-text{font-size:11px;line-height:14px;color:var(--muted);width:240px}
.card-link{font-size:13px;font-weight:700;color:var(--blue);line-height:16px}
.arrow-btn{width:34px;height:34px;border-radius:50%;background:var(--blue)}

/* portfolio */
.section-title{font-size:32px;letter-spacing:1px;color:var(--ink)}
.title-rule{height:4px;background:var(--blue)}
.tab{top:1887px;height:31px;font-size:15px;display:flex;align-items:center;justify-content:center;border:1px solid var(--blue)}
.tab.active{background:var(--blue);color:var(--white)}
.nav-arrow{top:1885px;width:51px;height:22px;border:1px solid var(--blue);display:flex;align-items:center;justify-content:center}
.folio-photo{top:1943px;width:138px;height:103px}
.folio-kicker{top:2057px;font-size:9px;color:var(--muted)}
.folio-title{top:2073px;font-size:12px;line-height:16px;color:var(--ink)}
.folio-link{top:2112px;font-size:12px;font-weight:700;color:var(--blue);letter-spacing:.5px}

/* about */
.about-photo{left:113px;top:2279px;width:442px;height:442px;border-radius:50%;background:radial-gradient(circle at 50% 45%,#ffb02e,#e8600e 55%,#a83208)}
.about-caption{left:113px;width:442px;top:2660px;text-align:center;color:var(--white);font-size:26px}
.more-box{left:224px;top:2714px;width:214px;height:43px;border-right:2px solid #ccc;border-bottom:2px solid #ccc;background:var(--white);color:var(--blue);font-size:13px;display:flex;align-items:center;justify-content:center;gap:8px}
.about-text{left:615px;top:2404px;width:364px;font-size:11.2px;line-height:18px;color:var(--muted);text-align:justify}

/* updates */
.updates{left:0;top:2900px;width:1200px;height:586px;background:linear-gradient(135deg,#3c9fe8,#2a92e2 60%,#3a9ee7)}
.updates-title{left:376px;top:2950px;font-size:27px;color:var(--white)}
.looking{left:376px;top:3026px;font-size:14px;color:var(--white)}
.chip{top:3020px;height:26px;border:1.5px solid var(--white);border-radius:6px;font-size:10px;color:var(--white);display:flex;align-items:center;justify-content:center}
.chip.on{background:var(--white);color:var(--ink)}
.field{left:376px;width:439px;border:1px solid rgba(255,255,255,.75);border-radius:3px}
.field-label{left:402px;font-size:10.5px;font-weight:700;color:var(--white)}
.address{left:857px;top:3109px;font-size:10px;font-weight:700;line-height:14px;color:var(--white)}
.agree{left:376px;top:3328px;font-size:10px;color:var(--white);display:flex;align-items:center;gap:6px}
.agree b{width:13px;height:13px;background:var(--white);display:inline-block;position:relative}
.submit{left:374px;top:3384px;width:121px;height:39px;background:var(--white);border-radius:3px;font-size:15px;display:flex;align-items:center;justify-content:center}

/* footer */
.footer{left:0;top:3486px;width:1200px;height:103px;background:var(--dark)}
.foot-nav{left:0;width:1200px;top:3510px;text-align:center;font-size:12.5px;font-weight:700;color:var(--white)}
.foot-nav span{margin:0 11px}
.privacy{left:0;width:1200px;top:3542px;text-align:center;font-size:12px;font-weight:700;color:var(--white)}
.bottom-bar{left:0;top:3589px;width:1200px;height:43px;background:var(--darker)}
.legal{left:164px;top:3606px;font-size:10px;color:var(--white)}
.foot-brand{left:0;width:1200px;top:3594px;text-align:center;font-weight:700;font-size:30px;letter-spacing:7px;color:var(--white)}
.social{top:3606px;width:13px;height:13px;background:#2d8fe0;border-radius:2px}
</style>
</head>
<body>

<!-- Hero -->
<div class="abs hero" role="img" aria-label="Architectural render of a modern arched building around a landscaped courtyard with people walking"></div>
<div class="abs brand">PELORIS</div>
<div class="abs hero-rule" style="top:80px"></div>
<nav class="abs main-nav"><span>Home</span>|<span>Property ⌄</span>|<span>Capital &amp; Finance</span>|<span>About us</span>|<span>Contact us</span></nav>
<div class="abs hero-rule" style="top:120px"></div>
<div class="abs bracket left"></div>
<div class="abs bracket right"></div>
<div class="abs tagline">You Dream it we do it</div>
<h1 class="abs hero-title">PROPERTY DEVELOPMENT &amp;<br>CONSTRUCTION</h1>
<a class="abs btn-invest">Investment</a>
<span class="abs dot on" style="left:895px"></span>
<span class="abs dot" style="left:925px"></span>
<span class="abs dot" style="left:953px"></span>
<div class="abs scroll-hint"><i></i></div>

<!-- Stats -->
<div class="abs stats" role="img" aria-label="Blue-tinted city skyscrapers"></div>
<div class="abs stat" style="left:159px;width:172px">500 Project<br>Delivered
  <svg width="24" height="22" viewBox="0 0 24 22" fill="none" stroke="#fff" stroke-width="2"><rect x="2" y="4" width="10" height="17"/><rect x="12" y="9" width="10" height="12"/><path d="M5 8h4M5 12h4M5 16h4M15 13h4M15 17h4"/></svg></div>
<div class="abs stat" style="left:361px;width:171px">15 Years<br>Experience
  <svg width="24" height="22" viewBox="0 0 24 22" fill="none" stroke="#fff" stroke-width="2"><rect x="2" y="4" width="20" height="17"/><path d="M2 9h20M7 1v5M17 1v5M6 13h2M11 13h2M16 13h2M6 17h2M11 17h2"/></svg></div>
<div class="abs stat" style="left:563px;width:233px">2000 Acqucition<br>Year
  <svg width="26" height="22" viewBox="0 0 26 22" fill="none" stroke="#fff" stroke-width="2"><path d="M2 21V12h6v9M10 21V8h6v13M18 21V14h6v7M4 8l6-5 5 3 7-5"/></svg></div>
<div class="abs stat" style="left:825px;width:184px">
  <svg width="20" height="26" viewBox="0 0 20 26"><path d="M10 1a8 8 0 0 1 8 8c0 6-8 16-8 16S2 15 2 9a8 8 0 0 1 8-8z" fill="#fff"/><circle cx="10" cy="9" r="3" fill="#3d8ad4"/></svg>
  <span>Sydney,<br>Australia.</span></div>

<!-- Service cards row 1 -->
<div class="abs card-photo" style="left:159px;top:977px;background:linear-gradient(180deg,#6fb3ec,#3c7fc4 60%,#6a9a6a)" role="img" aria-label="Office towers under a blue sky"></div>
<div class="abs card-label blue" style="left:193px;top:1121px;width:200px">Development &amp;<br>Construction</div>
<p class="abs card-text" style="left:171px;top:1176px">The standard chunk of Lorem Ipsum used since the 1500s is reproduced below for those</p>
<a class="abs card-link" style="left:171px;top:1240px">Checkout our on going<br>development Project</a>

<div class="abs card-photo" style="left:457px;top:977px;background:linear-gradient(180deg,#cfd8e0,#7c8f9f 50%,#3d4a55)" role="img" aria-label="Glass-roofed hotel restaurant interior"></div>
<div class="abs card-label" style="left:494px;top:1121px;width:190px;text-align:center;letter-spacing:1.5px">Hotel &amp;<br>Resturent</div>
<p class="abs card-text" style="left:468px;top:1176px">The standard chunk of Lorem Ipsum used since the 1500s is reproduced below for those</p>
<a class="abs card-link" style="left:469px;top:1249px">Visit our Hotel and Resturent</a>

<div class="abs card-photo" style="left:756px;top:977px;background:linear-gradient(180deg,#a5c9ea,#5b8bb6 55%,#4b6a84)" role="img" aria-label="Aerial view of a modern mixed-use development"></div>
<div class="abs card-label" style="left:789px;top:1126px;width:188px;text-align:center">Property Investment</div>
<p class="abs card-text" style="left:764px;top:1176px">The standard chunk of Lorem Ipsum used since the 1500s is reproduced below for those</p>
<a class="abs card-link" style="left:775px;top:1249px">Checkout Investment Projects</a>

<!-- Service cards row 2 -->
<div class="abs card-photo" style="left:159px;top:1325px;background:linear-gradient(180deg,#8cc4ee,#e8e8e4 45%,#2aa8d8)" role="img" aria-label="Apartment building with a swimming pool and palm trees"></div>
<div class="abs card-label" style="left:213px;top:1470px;width:170px;line-height:21.5px">Property<br>Management<br>&amp; Sell</div>
<p class="abs card-text" style="left:183px;top:1551px">The standard chunk of Lorem Ipsum used since the 1500s is reproduced below for those</p>
<a class="abs card-link" style="left:185px;top:1632px">Visit &nbsp;Current selling Property</a>

<div class="abs card-photo" style="left:457px;top:1325px;background:linear-gradient(160deg,#bcd6f0,#2a5fb0 55%,#163c7a)" role="img" aria-label="Blue glass office towers seen from below"></div>
<div class="abs card-label" style="left:503px;top:1470px;width:180px;text-align:center">Leasing &amp; Finance</div>
<p class="abs card-text" style="left:474px;top:1551px">The standard chunk of Lorem Ipsum used since the 1500s is reproduced below for those</p>
<a class="abs card-link" style="left:477px;top:1632px">Leasing hold Property</a>

<div class="abs card-photo" style="left:755px;top:1325px;background:linear-gradient(180deg,#eef2f4,#b8c2c8 55%,#4e7a3a)" role="img" aria-label="White modern house with glass walls and green plants"></div>
<div class="abs card-label" style="left:790px;top:1470px;width:188px;text-align:center">Rent &amp; Buy</div>
<p class="abs card-text" style="left:776px;top:1551px">The standard chunk of Lorem Ipsum used since the 1500s is reproduced below for those</p>
<a class="abs card-link" style="left:773px;top:1634px">Visit &nbsp;Rent Property</a>

<svg width="0" height="0" style="position:absolute"><defs><g id="arr"><path d="M9 17h16M20 12l5 5-5 5" fill="none" stroke="#fff" stroke-width="2"/></g></defs></svg>
<svg class="abs arrow-btn" style="left:365px;top:1238px" viewBox="0 0 34 34"><use href="#arr"/></svg>
<svg class="abs arrow-btn" style="left:679px;top:1238px" viewBox="0 0 34 34"><use href="#arr"/></svg>
<svg class="abs arrow-btn" style="left:976px;top:1238px" viewBox="0 0 34 34"><use href="#arr"/></svg>
<svg class="abs arrow-btn" style="left:381px;top:1623px" viewBox="0 0 34 34"><use href="#arr"/></svg>
<svg class="abs arrow-btn" style="left:676px;top:1623px" viewBox="0 0 34 34"><use href="#arr"/></svg>
<svg class="abs arrow-btn" style="left:967px;top:1623px" viewBox="0 0 34 34"><use href="#arr"/></svg>

<!-- Portfolio -->
<h2 class="abs section-title" style="left:154px;top:1800px">Portfolio</h2>
<div class="abs title-rule" style="left:154px;top:1841px;width:152px"></div>
<div class="abs tab active" style="left:155px;width:103px">Project</div>
<div class="abs tab" style="left:266px;width:103px">Hotel</div>
<div class="abs nav-arrow" style="left:900px"><svg width="26" height="8" viewBox="0 0 26 8"><path d="M25 4H2M6 1L2 4l4 3" fill="none" stroke="#1a86d6" stroke-width="1.3"/></svg></div>
<div class="abs nav-arrow" style="left:956px"><svg width="26" height="8" viewBox="0 0 26 8"><path d="M1 4h23M20 1l4 3-4 3" fill="none" stroke="#1a86d6" stroke-width="1.3"/></svg></div>

<div class="abs folio-photo" style="left:155px;background:linear-gradient(180deg,#5fa6e6,#d48a55 55%,#3a6a8a)" role="img" aria-label="Colourful apartment block"></div>
<div class="abs folio-photo" style="left:333px;background:linear-gradient(180deg,#3b6ea8,#d8c8a8 50%,#30a8d0)" role="img" aria-label="Residence with pool at dusk"></div>
<div class="abs folio-photo" style="left:513px;background:linear-gradient(180deg,#8bb8e6,#8a4a4a 55%,#9a9a9a)" role="img" aria-label="Brick apartment building on a corner"></div>
<div class="abs folio-photo" style="left:691px;background:linear-gradient(180deg,#eef0f2,#c8ccd0 55%,#d89050)" role="img" aria-label="Bright open-plan interior"></div>
<div class="abs folio-photo" style="left:870px;background:linear-gradient(180deg,#9bb8e0,#c27890 50%,#5e8a50)" role="img" aria-label="Street of townhouses"></div>

<div class="abs folio-kicker" style="left:162px">Lorem Ipsum</div>
<div class="abs folio-title" style="left:162px">variations of<br>passages</div>
<a class="abs folio-link" style="left:162px">View Project &nbsp;⟶</a>
<div class="abs folio-kicker" style="left:342px">Lorem Ipsum</div>
<div class="abs folio-title" style="left:342px">variations of<br>passages</div>
<a class="abs folio-link" style="left:342px">View Project &nbsp;⟶</a>
<div class="abs folio-kicker" style="left:522px">Lorem Ipsum</div>
<div class="abs folio-title" style="left:522px">variations of<br>passages</div>
<a class="abs folio-link" style="left:522px">View Project &nbsp;⟶</a>
<div class="abs folio-kicker" style="left:701px">Lorem Ipsum</div>
<div class="abs folio-title" style="left:701px">variations of<br>passages</div>
<a class="abs folio-link" style="left:701px">View Project &nbsp;⟶</a>
<div class="abs folio-kicker" style="left:883px">Lorem Ipsum</div>
<div class="abs folio-title" style="left:883px">variations of<br>passages</div>
<a class="abs folio-link" style="left:883px">View Project &nbsp;⟶</a>

<!-- About -->
<div class="abs about-photo" role="img" aria-label="Ornate hotel lounge interior in warm orange light"></div>
<div class="abs about-caption">Hotel Interior</div>
<a class="abs more-box">More about us <span>⟶</span></a>
<h2 class="abs section-title" style="left:615px;top:2344px;font-size:27px;letter-spacing:0">About Our Journey</h2>
<div class="abs title-rule" style="left:615px;top:2381px;width:151px;height:3px"></div>
<p class="abs about-text">Contrary to popular belief, Lorem Ipsum is not simply random text. It has roots in a piece of classical Latin literature from 45 BC, making it over 2000 years old. A Latin scholar at a small college looked up one of the more obscure Latin words, consectetur, from a Lorem Ipsum passage, and going through the cites of the word in classical literature, discovered the undoubtable source. Lorem Ipsum comes from sections 1.10.32 and 1.10.33 of "de Finibus Bonorum et Malorum" (The Extremes of Good and Evil), written in 45 BC. This book is a treatise on the theory of ethics, very popular during the Renaissance. The first line of Lorem Ipsum, "Lorem ipsum dolor sit amet..", comes from a line in section 1.10.32. The standard chunk of Lorem Ipsum used since the 1500s is reproduced below for those interested. Sections 1.10.32 and 1.10.33 from "de Finibus Bonorum et Malorum" are also reproduced in their exact original form, accompanied by English versions from a later translation.</p>

<!-- Updates -->
<div class="abs updates" role="img" aria-label="Blue-tinted street map of the inner city harbour area"></div>
<h2 class="abs updates-title">Get Latest Update of new Projects</h2>
<div class="abs looking">I am looing for...</div>
<div class="abs chip on" style="left:482px;width:89px">Latest update</div>
<div class="abs chip" style="left:584px;width:86px">Investing</div>
<div class="abs chip" style="left:691px;width:89px">Sell or Buy</div>
<div class="abs chip" style="left:794px;width:89px">Leasing</div>

<div class="abs field" style="top:3082px;height:27px"></div>
<div class="abs field-label" style="top:3076px">Name</div>
<div class="abs field" style="top:3124px;height:27px"></div>
<div class="abs field-label" style="top:3118px">Phone</div>
<div class="abs field" style="top:3173px;height:27px"></div>
<div class="abs field-label" style="top:3167px">Email</div>
<div class="abs field" style="top:3222px;height:68px"></div>
<div class="abs field-label" style="top:3216px">Message</div>

<svg class="abs" style="left:836px;top:3107px" width="14" height="34" viewBox="0 0 14 34"><path d="M7 1a5 5 0 0 1 5 5c0 4-5 9-5 9S2 10 2 6a5 5 0 0 1 5-5z" fill="#fff"/><circle cx="7" cy="6" r="2" fill="#2a92e2"/><circle cx="1.5" cy="28" r="2" fill="#fff"/></svg>
<div class="abs address">PO Box 1180, Sydney, NSW,<br>2000, Australia.</div>

<label class="abs agree"><b><svg width="13" height="13" viewBox="0 0 13 13"><path d="M2.5 7l3 3 5-7" fill="none" stroke="#1a86d6" stroke-width="2"/></svg></b>I agree with Term &amp; Condition</label>
<a class="abs submit">Submit</a>

<!-- Footer -->
<div class="abs footer"></div>
<nav class="abs foot-nav"><span>Home</span>|<span>Property</span>|<span>Capital &amp; Finance</span>|<span>About us</span>|<span>Contact us</span></nav>
<div class="abs privacy">See Privacy Policy &nbsp;⟶</div>
<div class="abs bottom-bar"></div>
<div class="abs legal">Term of Use | Privacy Policy</div>
<div class="abs foot-brand">PELORIS</div>
<span class="abs social" style="left:872px"></span>
<span class="abs social" style="left:903px"></span>
<span class="abs social" style="left:934px"></span>
<span class="abs social" style="left:965px"></span>
<span class="abs social" style="left:996px"></span>

</body>
</html>
```